NEW YORK Plumbing/utility company 10 year anniversary business card

Looking For simple back and front business card would like to include a few things in description
We offer 24/7 emergency service
residential
commercial
industrial
municipal
services offered
Plumbing
hydro excavation
hydro jetting
Well pumps
Sewer pumps
water mains
sewer mains

```html
<!DOCTYPE html>
<html lang="en">
<head>
<meta charset="utf-8">
<title>Kestrel Water &amp; Sewer – Business Card</title>
<link href="https://fonts.googleapis.com/css2?family=Arimo:wght@400;700&family=Montserrat:wght@700;800&display=swap" rel="stylesheet">
<style>
  :root{
    --blue:#1c5ea8;
    --red:#ec1c24;
    --white:#ffffff;
    --stage:#bdbec0;
    --ink:#1c5ea8;
  }
  *{box-sizing:border-box;margin:0;padding:0}
  html,body{width:826px;height:1200px;overflow:hidden}
  body{background:var(--stage);position:relative;font-family:"Arimo",Arial,sans-serif}

  .band{position:absolute;display:block}
  .band--blue{right:0;top:605px}
  .band--red{left:0;bottom:0}

  .card{position:absolute;width:368px;height:214px;background:var(--white);
        box-shadow:3px 4px 6px rgba(0,0,0,.35);overflow:hidden}
  .card--front{left:116px;top:679px}
  .card--back{left:338px;top:927px}
  .card__shapes{position:absolute;inset:0}

  /* brand name block */
  .brand{position:absolute;display:flex;align-items:center;gap:7px;color:var(--blue);
         font-family:"Montserrat",Arial,sans-serif;font-weight:800;text-transform:uppercase;line-height:1.05}
  .brand__dot{flex:none;border-radius:50%;background:var(--blue)}
  .card--front .brand{left:36px;top:78px;font-size:19px}
  .card--front .brand__dot{width:16px;height:16px}
  .card--back .brand{left:54px;top:20px;font-size:12px}
  .card--back .brand__dot{width:10px;height:10px}

  /* front contact */
  .person{position:absolute;left:223px;top:70px;width:140px;text-align:center}
  .person__name{color:var(--blue);font-weight:700;font-size:13px;letter-spacing:.2px}
  .person__role{color:var(--red);font-size:8px;letter-spacing:1.3px;margin-top:1px}
  .contact{position:absolute;left:228px;top:113px;list-style:none;color:var(--blue);font-size:9.5px}
  .contact li{display:flex;align-items:center;gap:5px;height:16px}
  .contact svg{width:8px;height:8px;flex:none}

  /* back left */
  .offer{position:absolute;left:57px;top:78px;width:106px;text-align:center;
         border-top:1.5px solid var(--red);border-bottom:1.5px solid var(--red);padding:4px 0 5px}
  .offer__lead{color:var(--blue);font-weight:700;font-size:19px;line-height:1}
  .offer__hours{color:var(--red);font-family:"Montserrat",Arial,sans-serif;font-weight:800;font-size:33px;line-height:1;letter-spacing:1px}
  .offer__note{color:var(--blue);font-weight:700;font-size:8.3px;margin-top:2px}
  .sectors{position:absolute;left:17px;top:165px;display:grid;grid-template-columns:102px 100px;row-gap:6px;list-style:none}
  .sectors li{color:var(--blue);font-weight:700;font-size:12px;display:flex;align-items:center;gap:4px}
  .sectors li::before{content:"";width:7px;height:7px;border-radius:50%;background:var(--red)}

  /* back right */
  .services__title{position:absolute;left:203px;top:21px;width:165px;height:23px;background:var(--red);
                   color:var(--white);font-weight:700;font-size:13px;line-height:23px;padding-left:17px;letter-spacing:.3px}
  .services__list{position:absolute;left:231px;top:52px;list-style:none}
  .services__list li{display:flex;align-items:center;gap:8px;color:var(--white);font-size:12.5px;height:20px}
  .services__list svg{width:11px;height:11px;flex:none}
</style>
</head>
<body>

<svg class="band band--blue" width="306" height="30" viewBox="0 0 306 30" aria-hidden="true"><polygon points="24,0 306,0 306,30 0,30" fill="var(--blue)"/></svg>
<svg class="band band--red" width="266" height="30" viewBox="0 0 266 30" aria-hidden="true"><polygon points="0,0 246,0 266,30 0,30" fill="var(--red)"/></svg>

<!-- Front -->
<section class="card card--front">
  <svg class="card__shapes" viewBox="0 0 368 214" aria-hidden="true">
    <polygon points="280,0 368,0 368,18 290,18" fill="var(--blue)"/>
    <polygon points="0,176 158,176 177,214 0,214" fill="var(--blue)"/>
    <polygon points="167,195 368,195 368,214 177,214" fill="var(--red)"/>
  </svg>
  <div class="brand"><span class="brand__dot"></span><span>Kestrel<br>Water &amp; Sewer</span></div>
  <div class="person">
    <p class="person__name">YOUR NAME</p>
    <p class="person__role">DESIGNATION</p>
  </div>
  <ul class="contact">
    <li><svg viewBox="0 0 10 10"><path d="M2 1l2 2-1 1.3c.6 1.2 1.5 2.1 2.7 2.7L7 6l2 2-1.3 1.3C4.5 9 1 5.5.7 2.3z" fill="var(--red)"/></svg>+0000 289 8165</li>
    <li><svg viewBox="0 0 10 10"><rect x="0" y="2" width="10" height="6.5" fill="var(--red)"/><path d="M0 2l5 3.5L10 2" stroke="#fff" fill="none"/></svg>info@companyname.com</li>
    <li><svg viewBox="0 0 10 10"><circle cx="5" cy="5" r="4.3" fill="none" stroke="var(--red)" stroke-width="1.2"/><path d="M.7 5h8.6M5 .7c-2.4 2.6-2.4 6 0 8.6M5 .7c2.4 2.6 2.4 6 0 8.6" stroke="var(--red)" fill="none" stroke-width=".9"/></svg>www.companyname.com</li>
  </ul>
</section>

<!-- Back -->
<section class="card card--back">
  <svg class="card__shapes" viewBox="0 0 368 214" aria-hidden="true">
    <rect x="220" y="0" width="148" height="214" fill="var(--blue)"/>
    <polygon points="203,44 220,44 220,55" fill="#9e1016"/>
  </svg>
  <div class="brand"><span class="brand__dot"></span><span>Kestrel<br>Water &amp; Sewer</span></div>
  <div class="offer">
    <p class="offer__lead">WE OFFER</p>
    <p class="offer__hours">24/7</p>
    <p class="offer__note">EMERGENCY SERVICE</p>
  </div>
  <ul class="sectors">
    <li>RESIDENTIAL</li><li>COMMERCIAL</li>
    <li>INDUSTRIAL</li><li>MUNICIPAL</li>
  </ul>
  <p class="services__title">SERVICES OFFERED</p>
  <ul class="services__list">
    <li><svg viewBox="0 0 12 12"><rect x=".7" y="1.5" width="9.5" height="9.5" fill="none" stroke="#fff" stroke-width="1.3"/><path d="M3 6l2.2 2.3L11.3 1" fill="none" stroke="#fff" stroke-width="1.5"/></svg>Plumbing</li>
    <li><svg viewBox="0 0 12 12"><rect x=".7" y="1.5" width="9.5" height="9.5" fill="none" stroke="#fff" stroke-width="1.3"/><path d="M3 6l2.2 2.3L11.3 1" fill="none" stroke="#fff" stroke-width="1.5"/></svg>Hydro Excavation</li>
    <li><svg viewBox="0 0 12 12"><rect x=".7" y="1.5" width="9.5" height="9.5" fill="none" stroke="#fff" stroke-width="1.3"/><path d="M3 6l2.2 2.3L11.3 1" fill="none" stroke="#fff" stroke-width="1.5"/></svg>Hydro Jetting</li>
    <li><svg viewBox="0 0 12 12"><rect x=".7" y="1.5" width="9.5" height="9.5" fill="none" stroke="#fff" stroke-width="1.3"/><path d="M3 6l2.2 2.3L11.3 1" fill="none" stroke="#fff" stroke-width="1.5"/></svg>Well Pumps</li>
    <li><svg viewBox="0 0 12 12"><rect x=".7" y="1.5" width="9.5" height="9.5" fill="none" stroke="#fff" stroke-width="1.3"/><path d="M3 6l2.2 2.3L11.3 1" fill="none" stroke="#fff" stroke-width="1.5"/></svg>Sewer Pumps</li>
    <li><svg viewBox="0 0 12 12"><rect x=".7" y="1.5" width="9.5" height="9.5" fill="none" stroke="#fff" stroke-width="1.3"/><path d="M3 6l2.2 2.3L11.3 1" fill="none" stroke="#fff" stroke-width="1.5"/></svg>Water Mains</li>
    <li><svg viewBox="0 0 12 12"><rect x=".7" y="1.5" width="9.5" height="9.5" fill="none" stroke="#fff" stroke-width="1.3"/><path d="M3 6l2.2 2.3L11.3 1" fill="none" stroke="#fff" stroke-width="1.5"/></svg>Sewer Mains</li>
  </ul>
</section>

</body>
</html>
```